To design a brand identity that is simple and creative with 'Valdor' as the brand name, I like modern simple fonts like helvetica neue, I want to print both sides of the card, I am open to dark front and white back, but the design needs to transfer well to letter heads and email signatures, I am looking for sophisticated and elegant, but open minded about clever and off the wall, I do not do 'boring' Valdor Holdings is the mother company for a small group, specialising in Management & consulting, Software development and construction, we have a high level of integrity, we are transparent and accountable for what we do. my images are provided as a guide only, Im not expecting them to be just copied, Im looking for a creator and passionate thinker, who will put life into their work.

Target Market(s)

usually business minded people who are looking for something different in me, such as leadership, confidence and focus with thinking that is per haps a little outside the box..

Industry/Entity Type

Construction

Requirements
Must have
• clean, minmalistic
Nice to have
• custom logo
Should not have
• boring, traditional

```html
<!DOCTYPE html>
<html lang="en">
<head>
<meta charset="utf-8">
<title>Valdor — Business Card</title>
<link href="https://fonts.googleapis.com/css2?family=Open+Sans:ital,wght@0,300;0,400;0,600;0,700;1,400&display=swap" rel="stylesheet">
<style>
  :root {
    --page: #e4e5ea;
    --charcoal: #262626;
    --charcoal-deep: #151515;
    --brand-orange: #f0622a;
    --coral: #e8473f;
    --ink: #333333;
    --muted: #8a8a8a;
    --white: #ffffff;
    --gold: #f2a516;
    --panel-warm: #e8452c;
    --panel-cool: #17917c;
  }
  * { box-sizing: border-box; margin: 0; padding: 0; }
  html, body {
    width: 1200px; height: 987px; overflow: hidden;
    background: var(--page);
    font-family: "Open Sans", Helvetica, Arial, sans-serif;
  }
  .card {
    position: absolute; left: 190px;
    width: 820px; height: 450px;
    border-radius: 34px; overflow: hidden;
    box-shadow: 0 6px 18px rgba(0,0,0,0.18);
  }
  /* Front */
  .card--front {
    top: 22px;
    background: linear-gradient(160deg, var(--charcoal) 0%, var(--charcoal-deep) 100%);
    color: var(--white);
  }
  .card__panel { position: absolute; inset: 0; width: 100%; height: 100%; }
  .brand { position: absolute; left: 60px; top: 115px; display: flex; align-items: center; gap: 20px; }
  .brand__dot { width: 56px; height: 56px; border-radius: 50%; background: var(--brand-orange); }
  .brand__name {
    font-weight: 300; font-size: 96px; line-height: 1; letter-spacing: 1px;
    color: var(--brand-orange);
  }
  .brand__tagline {
    position: absolute; left: 140px; top: 232px;
    font-style: italic; font-weight: 400;
    font-size: 19px; color: var(--muted);
  }
  .person { position: absolute; right: 36px; top: 250px; text-align: right; }
  .person__name { font-weight: 700; font-size: 30px; line-height: 1.2; }
  .person__title { font-size: 22px; font-weight: 400; line-height: 1.4; }
  .contact {
    position: absolute; left: 50px; bottom: 48px;
    font-size: 17px; line-height: 1.5; display: flex; align-items: flex-end; gap: 18px;
  }
  .contact__row { display: flex; align-items: center; gap: 8px; }
  .contact__icon { width: 16px; height: 16px; }
  .contact__divider { width: 1px; height: 46px; background: var(--white); }
  /* Back */
  .card--back { top: 510px; background: var(--white); }
  .wordmark {
    position: absolute; left: 160px; top: 40px;
    font-weight: 300; font-size: 170px; line-height: 1; letter-spacing: 3px;
    color: var(--brand-orange);
  }
  .services {
    position: absolute; left: 70px; top: 268px;
    list-style: none; color: var(--coral); font-size: 22px; line-height: 1.45;
    display: flex; flex-wrap: wrap; column-gap: 26px; width: 640px;
  }
  .services li::before { content: "•"; color: var(--muted); margin-right: 8px; }
  .website {
    position: absolute; left: 70px; top: 362px;
    font-size: 26px; letter-spacing: 8px; color: var(--ink);
  }
</style>
</head>
<body>
  <section class="card card--front">
    <svg class="card__panel" viewBox="0 0 820 450" preserveAspectRatio="none" role="img" aria-label="Colour panel in warm red to teal tones">
      <defs>
        <linearGradient id="panelGradient" x1="0" y1="0" x2="0.6" y2="1">
          <stop offset="0" stop-color="var(--panel-warm)"/>
          <stop offset="1" stop-color="var(--panel-cool)"/>
        </linearGradient>
      </defs>
      <polygon points="520,0 820,0 820,450 640,450" fill="url(#panelGradient)"/>
    </svg>
    <div class="brand">
      <span class="brand__dot"></span>
      <span class="brand__name">Valdor</span>
    </div>
    <p class="brand__tagline">…building what comes next.</p>
    <div class="person">
      <p class="person__name">Your Name</p>
      <p class="person__title">Title</p>
    </div>
    <div class="contact">
      <div>
        <p class="contact__row">
          <svg class="contact__icon" viewBox="0 0 16 16" aria-hidden="true"><circle cx="8" cy="8" r="7.5" fill="var(--gold)"/><path d="M5 4.5c0 3.5 3 6.5 6.5 6.5l.8-1.6-2-1-1 1c-1-.5-2-1.5-2.5-2.5l1-1-1-2z" fill="var(--charcoal)"/></svg>
          +61 0400 512 694
        </p>
        <p class="contact__row">
          <svg class="contact__icon" viewBox="0 0 16 16" aria-hidden="true"><rect x="0.5" y="3" width="15" height="10" rx="1.5" fill="var(--gold)"/><path d="M1.5 4l6.5 5 6.5-5" fill="none" stroke="var(--charcoal)" stroke-width="1.3"/></svg>
          names@valdor.holdings
        </p>
      </div>
      <span class="contact__divider"></span>
      <p>PO Box 418 Perth 6031</p>
    </div>
  </section>

  <section class="card card--back">
    <p class="wordmark">Valdor</p>
    <ul class="services">
      <li>Management &amp; Consulting</li>
      <li>Software Development</li>
      <li>Construction</li>
    </ul>
    <p class="website">www.valdor.com</p>
  </section>
</body>
</html>
```